Wheels Bring Trade - Two sided invitation to encourage bike friendly businesses

Pedal Haven is a charitable trust who want to grow everyday bike use. One way to do that is help businesses understand that 'Wheels Bring Trade'. We want a postcard sized 'invitation' that bike users can give to their favourite businesses, inviting them to find out more about all the benefits of attracting bike users to their business and becoming a 'Pedal Haven Business'. We are currently finalising copy, so the attached is indicative but not final copy. The docx file is the words, the png is indicative of the type of infographic we might want to feature.
I'm also attaching a mock up of our window sticker for businesses, and some social shares featuring photographic images which we have available to use. This will give you an idea of our branding to date. Our extended branding concept (which we will use when we re-do our website) is based on icons, so I'm open to seeing icon focused designs also.
The feel needs to be inviting, credible, enticing, business like, noticeable, with a strong call to action.

Target Market(s)

Small business operators: retail, cafes, etc; also managers of larger chains such as supermarkets, gyms, etc.

Industry/Entity Type

Non Profit

Font styles to use
Serif
Other font styles liked:
• Logo is done in Raleway, so need compatible font.

Colors
9ccb3b

Requirements
Must have
• Two Sides
• Use the copy provided
• Strong call to action - visiting website
• Use our colours
• A6 sized cards
Nice to have
• Compelling images and/or infographic
• Consistency with circles / curves used in other branding.
Should not have
• Not bland, not something that will get lost on the recipients desk or counter.

```html
<!DOCTYPE html>
<html lang="en">
<head>
<meta charset="utf-8">
<title>Pedal Haven – Invitation Postcard</title>
<link href="https://fonts.googleapis.com/css2?family=Raleway:ital,wght@0,400;0,500;0,600;0,700;0,800;1,700&display=swap" rel="stylesheet">
<style>
  :root {
    --green: #3bb54a;
    --green-light: #9ccb3b;
    --green-pale: #e9f5e4;
    --grey-bg: #e6e7e8;
    --grey-mid: #8a8c8e;
    --grey-dark: #58595b;
    --ink: #231f20;
    --white: #ffffff;
    --page: #efeeec;
  }
  * { box-sizing: border-box; margin: 0; padding: 0; }
  html, body { width: 981px; height: 1200px; overflow: hidden; }
  body {
    background: var(--page);
    font-family: "Raleway", Arial, sans-serif;
    position: relative;
  }
  .postcard {
    position: absolute;
    left: 130px;
    width: 720px;
    height: 510px;
    background: var(--grey-bg);
    overflow: hidden;
    box-shadow: 0 2px 6px rgba(0,0,0,.18);
  }
  .postcard--front { top: 60px; }
  .postcard--back { top: 620px; }

  .layer { position: absolute; inset: 0; }

  /* ---------- Front ---------- */
  .front-heading {
    position: absolute; left: 30px; top: 30px; width: 300px;
    color: var(--white); font-weight: 700; font-size: 31px; line-height: 1.32;
  }
  .front-heading em { font-style: italic; }
  .hero-photo {
    position: absolute; left: 304px; top: 24px; width: 404px; height: 404px;
    border-radius: 50%; border: 12px solid var(--white);
    background: radial-gradient(circle at 40% 40%, #c9b8a2 0%, #8c8f8a 45%, #5f6d72 100%);
  }
  .info-band {
    position: absolute; left: 230px; right: 0; top: 396px; height: 68px;
    background: var(--white);
  }
  .brand {
    position: absolute; display: flex; align-items: center;
  }
  .brand__circle {
    border-radius: 50%; background: var(--white); border: 4px solid var(--grey-dark);
    position: relative; z-index: 2; flex: 0 0 auto;
  }
  .brand__tab {
    background: var(--green); color: var(--white); font-weight: 400;
    clip-path: polygon(0 0, 92% 0, 100% 50%, 92% 100%, 0 100%);
  }
  .brand--front { left: 22px; top: 368px; }
  .brand--front .brand__circle { width: 116px; height: 116px; }
  .brand--front .brand__tab {
    margin-left: -12px; padding: 6px 30px 6px 24px; font-size: 27px; line-height: 1.05; height: 74px;
    display: flex; align-items: center; width: 160px;
  }
  .compare { position: absolute; top: 404px; display: flex; align-items: flex-start; gap: 6px; }
  .compare--car { left: 318px; }
  .compare--bikes { left: 508px; }
  .compare__art { display: block; border-radius: 4px; }
  .compare__art--car { width: 108px; height: 26px; background: linear-gradient(#c8c9cb, #9c9ea1); border-radius: 14px 22px 6px 6px; }
  .compare__art--bikes { width: 108px; height: 30px; background: linear-gradient(#d7d8da, #b4b6b8); }
  .measure {
    width: 108px; margin-top: 8px; border-top: 1px solid var(--grey-dark);
    font-size: 8px; color: var(--grey-dark); text-align: center; padding-top: 1px; position: relative;
  }
  .measure::before, .measure::after {
    content: ""; position: absolute; top: -4px; width: 1px; height: 7px; background: var(--grey-dark);
  }
  .measure::before { left: 0; } .measure::after { right: 0; }
  .price-tag {
    margin-top: 8px; transform: rotate(22deg);
    border: 2px solid var(--green); border-radius: 4px 12px 12px 4px;
    color: var(--green); font-weight: 700; font-size: 12px; line-height: 1.05;
    padding: 4px 8px; text-align: center; background: var(--white);
  }
  .front-url {
    position: absolute; right: 30px; bottom: 16px;
    color: var(--green); font-size: 17px; font-weight: 500;
  }

  /* ---------- Back ---------- */
  .back-heading {
    position: absolute; top: 30px; left: 0; right: 0; text-align: center;
    color: var(--white); font-weight: 700; font-size: 27px; letter-spacing: .3px;
  }
  .benefit {
    position: absolute; display: flex; align-items: flex-start; gap: 12px;
    color: var(--white); font-size: 15px; line-height: 1.3;
  }
  .benefit__icon {
    flex: 0 0 44px; width: 44px; height: 44px; border-radius: 50%;
    background: var(--white); display: flex; align-items: center; justify-content: center;
    margin-top: 4px;
  }
  .benefit__icon svg { width: 26px; height: 26px; }
  .benefit__text { display: block; }
  .b1 { left: 22px; top: 86px; }
  .b1 .benefit__text { width: 138px; }
  .b2 { left: 240px; top: 86px; }
  .b2 .benefit__text { width: 150px; }
  .b3 { left: 478px; top: 86px; }
  .b3 .benefit__text { width: 170px; }
  .b4 { left: 116px; top: 176px; }
  .b4 .benefit__text { width: 160px; }
  .b5 { left: 370px; top: 176px; }
  .b5 .benefit__text { width: 210px; }

  .study {
    position: absolute; left: 60px; right: 60px; top: 362px;
    text-align: center; color: var(--ink); font-size: 15px; line-height: 1.55;
  }
  .nudge {
    position: absolute; left: 0; right: 0; top: 422px; text-align: center;
    color: var(--green); font-size: 15px;
  }
  .nudge strong { font-weight: 700; }
  .brand--back { left: 16px; top: 460px; }
  .brand--back .brand__circle { width: 44px; height: 44px; border-width: 2px; }
  .brand--back .brand__tab {
    margin-left: -6px; padding: 2px 16px 2px 12px; font-size: 12px; line-height: 1.05;
    background: var(--white); color: var(--green);
    clip-path: none; width: 70px;
  }
  .cta-bar {
    position: absolute; left: 148px; right: 0; top: 468px; height: 32px;
    background: var(--green); color: var(--white);
    font-size: 19px; font-weight: 500; display: flex; align-items: center; padding-left: 12px;
    white-space: nowrap;
  }
  .cta-bar strong { font-weight: 700; margin-left: 6px; }
</style>
</head>
<body>

<!-- Front side -->
<section class="postcard postcard--front">
  <svg class="layer" viewBox="0 0 720 510" aria-hidden="true">
    <path d="M0 0 H720 V250 C640 200 560 180 470 190 C330 205 190 270 0 196 Z" fill="#ffffff"/>
    <path d="M0 0 H720 V236 C640 186 560 168 470 176 C330 190 190 255 0 184 Z" fill="var(--green)"/>
  </svg>
  <h1 class="front-heading">Why make biking customers <em>and their dollars</em> welcome?</h1>
  <div class="hero-photo" role="img" aria-label="Photo of two smiling cyclists in helmets riding through a colourful laneway"></div>
  <div class="info-band"></div>
  <div class="brand brand--front">
    <div class="brand__circle"></div>
    <div class="brand__tab">Pedal Haven</div>
  </div>
  <div class="compare compare--car">
    <div>
      <span class="compare__art compare__art--car" role="img" aria-label="Side view of a parked car"></span>
      <div class="measure">13m²</div>
    </div>
    <div class="price-tag">$27<br>per hour</div>
  </div>
  <div class="compare compare--bikes">
    <div>
      <span class="compare__art compare__art--bikes" role="img" aria-label="Six parked bicycles side by side"></span>
      <div class="measure">13m²</div>
    </div>
    <div class="price-tag">$97<br>per hour</div>
  </div>
  <div class="front-url">www.pedalhaven.org</div>
</section>

<!-- Back side -->
<section class="postcard postcard--back">
  <svg class="layer" viewBox="0 0 720 510" aria-hidden="true">
    <path d="M0 0 H720 V260 C560 350 160 350 0 260 Z" fill="#ffffff"/>
    <path d="M0 0 H720 V246 C560 334 160 334 0 246 Z" fill="var(--green)"/>
  </svg>
  <svg class="layer" viewBox="0 0 720 510" role="img" aria-label="Faded photo of a cyclist riding down a street, tinted green">
    <defs>
      <radialGradient id="tint" cx="55%" cy="35%" r="60%">
        <stop offset="0" stop-color="#ffffff" stop-opacity=".16"/>
        <stop offset="1" stop-color="#ffffff" stop-opacity="0"/>
      </radialGradient>
    </defs>
    <path d="M0 0 H720 V246 C560 334 160 334 0 246 Z" fill="url(#tint)"/>
  </svg>

  <h2 class="back-heading">WHY WELCOME BIKES?</h2>

  <div class="benefit b1">
    <span class="benefit__icon"><svg viewBox="0 0 26 26"><path d="M9 5 L13 9 L17 5 Z" fill="var(--grey-dark)"/><circle cx="13" cy="16" r="8" fill="var(--grey-dark)"/><text x="13" y="20.5" text-anchor="middle" font-size="12" font-weight="700" fill="#fff" font-family="Raleway, sans-serif">$</text></svg></span>
    <span class="benefit__text">Biking customers spend where parking is easy.</span>
  </div>
  <div class="benefit b2">
    <span class="benefit__icon"><svg viewBox="0 0 26 26"><rect x="5" y="8" width="16" height="15" rx="1" fill="var(--grey-dark)"/><path d="M9 9 V6 a4 4 0 0 1 8 0 V9" fill="none" stroke="var(--grey-dark)" stroke-width="1.6"/></svg></span>
    <span class="benefit__text">They spend locally and often, as they carry smaller loads.</span>
  </div>
  <div class="benefit b3">
    <span class="benefit__icon"><svg viewBox="0 0 26 26"><circle cx="7" cy="18" r="4.5" fill="none" stroke="var(--grey-dark)" stroke-width="1.8"/><circle cx="19" cy="18" r="4.5" fill="none" stroke="var(--grey-dark)" stroke-width="1.8"/><path d="M7 18 L11 11 H17 L19 18 M11 11 L14 18" fill="none" stroke="var(--grey-dark)" stroke-width="1.8"/><circle cx="15" cy="6" r="2" fill="var(--grey-dark)"/></svg></span>
    <span class="benefit__text">Biking customers pass by slower, so see what your business offers.</span>
  </div>
  <div class="benefit b4">
    <span class="benefit__icon"><svg viewBox="0 0 26 26"><circle cx="7" cy="10" r="3" fill="var(--grey-dark)"/><circle cx="19" cy="10" r="3" fill="var(--grey-dark)"/><circle cx="13" cy="8" r="3.5" fill="var(--grey-dark)"/><path d="M2 20 a5 5 0 0 1 10 0 Z M14 20 a5 5 0 0 1 10 0 Z M7 21 a6 6 0 0 1 12 0 Z" fill="var(--grey-dark)"/></svg></span>
    <span class="benefit__text">They tell their friends where is good to park and shop.</span>
  </div>
  <div class="benefit b5">
    <span class="benefit__icon"><svg viewBox="0 0 26 26"><path d="M13 21 C4 14 3 10 5 7 a4.5 4.5 0 0 1 8 1 a4.5 4.5 0 0 1 8 -1 C23 10 22 14 13 21 Z" fill="none" stroke="var(--grey-dark)" stroke-width="1.8"/><path d="M13 21 V25" stroke="var(--grey-dark)" stroke-width="1.8"/></svg></span>
    <span class="benefit__text">It helps the environment, bikers' health and budgets &amp; that's always welcome.</span>
  </div>

  <p class="study">A Melbourne study showed swapping a car park for six bike parks could bump the space's spend from $27 to $97 an hour.</p>
  <p class="nudge">Every bike parked at someone else's business <strong>isn't shopping at yours.</strong></p>

  <div class="brand brand--back">
    <div class="brand__circle"></div>
    <div class="brand__tab">Pedal Haven</div>
  </div>
  <div class="cta-bar">How to welcome bikes? visit <strong>www.pedalhaven.org</strong></div>
</section>

</body>
</html>
```